Cedar Row Maintenance and Concierge Flyer

We need a flyer for cedar row maintenance and concierge service. We specialize in and provide residential maintenance and errand services to retired and semi retired persons living in the Lake Norman area. The services we include:
Lighting and plumbing repairs
Ceiling fan installation
Handicap accessories
Locks and security
Picture hanging
Hang blinds
Furniture arrangement / assembly
Pressure washing
Battery Jump start
and more...

Our Concierge services include:
Errand running
Grocery shopping
Wellness Checks
Dog Walk
Garbage Collection
and more...

We offer monthly service agreements and 24/7 access
Call text or e-mail for more information
704.555.0187
1cedarrowmaint@quillpostmail.com

The design should invoke a sense of trust and a customer service driven mission

Target Market(s)

Residential maintenance

Industry/Entity Type

Property Maintenance

Contact Information for Business Card

Derek Halvorsen
48176 Quimby Ferrel Rd.
Cornelius NC 28031
704.555.0187
with uploaded logo

Requirements
Nice to have
• Would like a postcard size flyer. Front and back
Should not have
• No pics of of people wearing hard hats or pics of blueprints. No pics of commercial or industrial maintenance.

```html
<!DOCTYPE html>
<html lang="en">
<head>
<meta charset="utf-8">
<title>Cedar Row Maintenance &amp; Concierge – Postcard Flyer</title>
<link rel="stylesheet" href="https://fonts.googleapis.com/css2?family=Arimo:wght@400;700&display=swap">
<style>
  :root {
    --sheet: #ffffff;
    --sheet-line: #555555;
    --label: #8a8a8a;
    --card: #f6efd2;
    --card-line: #7a7a7a;
    --ink: #2b2b2b;
    --red: #e1323e;
    --band-dark: #2f2f31;
    --band-red: #e8303d;
    --brand: #5a5a5a;
    --photo-a: #3f6fb8;
    --photo-b: #1f3f7a;
    --glyph: #ffffff;
  }
  * { box-sizing: border-box; margin: 0; padding: 0; }
  html, body { width: 846px; height: 1200px; overflow: hidden; background: var(--sheet); }
  body { font-family: "Arimo", Arial, sans-serif; color: var(--ink); }

  .sheet { position: relative; width: 846px; height: 1200px; border: 1px solid var(--sheet-line); }
  .side-label { position: absolute; left: 0; width: 100%; text-align: center; font-size: 33px; color: var(--label); }
  .side-label.front-label { top: 32px; }
  .side-label.back-label { top: 1137px; }

  .card { position: absolute; left: 38px; width: 752px; background: var(--card); border: 1px solid var(--card-line); overflow: hidden; }
  .card.front { top: 79px; height: 501px; }
  .card.back { top: 622px; height: 499px; }

  /* Front */
  .brand { position: absolute; left: 96px; top: 52px; display: flex; align-items: center; gap: 12px; color: var(--brand); font-weight: 400; }
  .brand-mark { width: 68px; height: 68px; border-radius: 50%; background: var(--red); }
  .brand-name { font-size: 40px; line-height: 1; letter-spacing: 0.5px; }
  .brand-sub { font-size: 14px; margin-top: 6px; letter-spacing: 0.4px; }

  .service-band { position: absolute; left: 0; top: 156px; width: 752px; height: 193px;
    background: linear-gradient(90deg, var(--band-dark) 0%, var(--band-dark) 58%, #8c2a33 75%, var(--band-red) 100%); }
  .tile { position: absolute; width: 71px; height: 71px; }
  .tile .glyph { fill: none; stroke: var(--glyph); stroke-width: 3.5; stroke-linecap: round; stroke-linejoin: round; }
  .tile .solid { fill: var(--glyph); stroke: none; }

  .hero-photo { position: absolute; left: 440px; top: 159px; width: 312px; height: 342px;
    background: radial-gradient(ellipse at 60% 40%, var(--photo-a) 0%, var(--photo-b) 80%);
    clip-path: polygon(95px 0, 205px 0, 312px 150px, 312px 342px, 70px 342px, 0 270px, 12px 190px, 82px 185px); }

  .intro { position: absolute; left: 25px; top: 362px; width: 400px; font-size: 12.2px; line-height: 1.3; color: var(--ink); }
  .intro p + p { margin-top: 14px; text-align: justify; }

  /* Back */
  .services { position: absolute; top: 56px; }
  .services.maintenance { left: 38px; }
  .services.concierge { left: 364px; }
  .services h2 { color: var(--red); font-size: 17px; font-weight: 700; line-height: 25px; margin-bottom: 1px; }
  .services ul { list-style: none; }
  .services li { font-size: 17.5px; line-height: 26.4px; }
  .services li::before { content: "\2611"; margin-right: 6px; }
  .services li.more { padding-left: 20px; }
  .services li.more::before { content: none; }

  .offer-banner { position: absolute; left: 219px; top: 372px; width: 533px; height: 27px; }
  .offer-banner svg { position: absolute; left: 0; top: 0; }
  .offer-banner span { position: absolute; left: 16px; top: 0; line-height: 27px; color: #fff; font-weight: 700; font-size: 17px; }

  .contact-prompt { position: absolute; right: 346px; top: 408px; text-align: right; font-size: 20.5px; font-weight: 700; line-height: 31px; }
  .contact-divider { position: absolute; left: 420px; top: 409px; width: 1px; height: 56px; background: var(--ink); }
  .contact-line { position: absolute; left: 440px; display: flex; align-items: center; gap: 10px; font-weight: 700; }
  .contact-line.phone { top: 404px; font-size: 36px; }
  .contact-line.email { top: 447px; font-size: 13.5px; }
</style>
</head>
<body>
<div class="sheet">
  <div class="side-label front-label">front</div>

  <section class="card front">
    <div class="brand">
      <div class="brand-mark"></div>
      <div>
        <div class="brand-name">Cedar Row</div>
        <div class="brand-sub">MAINTENANCE &amp; CONCIERGE</div>
      </div>
    </div>

    <div class="service-band">
      <svg class="tile" style="left:25px;top:18px" viewBox="0 0 71 71" role="img" aria-label="Garbage bin icon">
        <rect width="71" height="71" fill="#f47c20"/>
        <rect class="solid" x="18" y="16" width="35" height="6" rx="2"/>
        <path class="solid" d="M21 25 H50 L47 56 H24 Z"/>
      </svg>
      <svg class="tile" style="left:107px;top:18px" viewBox="0 0 71 71" role="img" aria-label="Armchair icon">
        <rect width="71" height="71" fill="#b4505a"/>
        <path class="glyph" d="M22 36 V26 Q22 20 28 20 H43 Q49 20 49 26 V36"/>
        <path class="glyph" d="M16 34 H24 V42 H47 V34 H55 V50 H16 Z"/>
        <path class="glyph" d="M20 50 V55 M51 50 V55"/>
      </svg>
      <svg class="tile" style="left:193px;top:18px" viewBox="0 0 71 71" role="img" aria-label="Faucet icon">
        <rect width="71" height="71" fill="#3a8fd0"/>
        <rect class="solid" x="12" y="24" width="28" height="10"/>
        <path class="solid" d="M34 24 H46 Q52 24 52 30 V38 H44 V34 H34 Z"/>
        <rect class="solid" x="26" y="15" width="16" height="5" rx="2"/>
        <rect class="solid" x="32" y="18" width="4" height="7"/>
        <path class="solid" d="M48 44 Q52 50 48 54 Q44 50 48 44 Z"/>
      </svg>
      <svg class="tile" style="left:277px;top:18px" viewBox="0 0 71 71" role="img" aria-label="Ceiling fan icon">
        <rect width="71" height="71" fill="#8cc63f"/>
        <path class="glyph" d="M35.5 14 V30"/>
        <circle class="solid" cx="35.5" cy="34" r="5"/>
        <path class="solid" d="M30 32 L10 30 L10 36 Z M41 32 L61 30 L61 36 Z M33 38 L24 52 L29 54 Z M38 38 L47 52 L42 54 Z"/>
      </svg>
      <svg class="tile" style="left:359px;top:18px" viewBox="0 0 71 71" role="img" aria-label="Stethoscope icon">
        <rect width="71" height="71" fill="#5bc8ee"/>
        <path class="glyph" d="M24 16 V30 Q24 42 33 42 Q42 42 42 30 V16"/>
        <path class="glyph" d="M33 42 V50 Q33 57 41 57 Q49 57 49 50 V46"/>
        <circle class="glyph" cx="49" cy="41" r="5"/>
      </svg>
      <svg class="tile" style="left:440px;top:18px" viewBox="0 0 71 71" role="img" aria-label="Grocery bag icon">
        <rect width="71" height="71" fill="#f47c20"/>
        <path class="solid" d="M20 30 H51 L48 58 H23 Z"/>
        <path class="glyph" d="M28 30 V22 M36 30 V16 M43 30 V24"/>
      </svg>
      <svg class="tile" style="left:25px;top:101px" viewBox="0 0 71 71" role="img" aria-label="Padlock icon">
        <rect width="71" height="71" fill="#2fa0dc"/>
        <path class="glyph" d="M26 33 V26 Q26 16 35.5 16 Q45 16 45 26 V33"/>
        <rect class="solid" x="20" y="32" width="31" height="24" rx="3"/>
        <circle cx="35.5" cy="43" r="3" fill="#2fa0dc"/>
      </svg>
      <svg class="tile" style="left:107px;top:101px" viewBox="0 0 71 71" role="img" aria-label="Wheelchair access icon">
        <rect width="71" height="71" fill="#1c4f9c"/>
        <circle class="solid" cx="30" cy="16" r="4"/>
        <path class="glyph" d="M30 23 V38 H44 L48 52"/>
        <path class="glyph" d="M30 30 H40"/>
        <path class="glyph" d="M24 34 A12 12 0 1 0 41 48"/>
      </svg>
      <svg class="tile" style="left:193px;top:101px" viewBox="0 0 71 71" role="img" aria-label="Light bulb icon">
        <rect width="71" height="71" fill="#f47c20"/>
        <path class="glyph" d="M35.5 10 V18"/>
        <rect class="solid" x="30" y="17" width="11" height="8"/>
        <circle class="solid" cx="35.5" cy="41" r="16"/>
      </svg>
      <svg class="tile" style="left:277px;top:101px" viewBox="0 0 71 71" role="img" aria-label="Picture frame icon">
        <rect width="71" height="71" fill="#f2c12e"/>
        <path class="glyph" d="M26 24 L35.5 14 L45 24"/>
        <rect class="glyph" x="15" y="24" width="41" height="32"/>
        <path class="solid" d="M20 51 L30 39 L37 46 L43 40 L51 51 Z"/>
      </svg>
      <svg class="tile" style="left:359px;top:101px" viewBox="0 0 71 71" role="img" aria-label="Pressure washer icon">
        <rect width="71" height="71" fill="#b4505a"/>
        <path class="glyph" d="M10 14 L34 30 M14 22 L20 16"/>
        <path class="glyph" d="M38 32 L58 40 M38 34 L52 48 M38 30 L60 30" stroke-dasharray="3 4"/>
        <path class="glyph" d="M6 54 H65 M20 54 L14 66 M35.5 54 V66 M51 54 L57 66" stroke-width="2"/>
      </svg>
      <svg class="tile" style="left:440px;top:101px" viewBox="0 0 71 71" role="img" aria-label="Leash icon for dog walking">
        <rect width="71" height="71" fill="#1fa37a"/>
        <circle class="glyph" cx="22" cy="22" r="7"/>
        <path class="glyph" d="M27 27 Q40 40 52 50"/>
        <circle class="solid" cx="53" cy="51" r="4"/>
      </svg>
    </div>

    <div class="hero-photo" role="img" aria-label="Photo of a smiling handyman in blue overalls holding a clipboard, giving a thumbs up"></div>

    <div class="intro">
      <p>Are you at your wits end trying to find time to get everything done in the limited fre time you have? Yes? Then Cedar Row can:</p>
      <p>Help you free up your time; do the routine tasks that take up valuable free time; so you can use your vacation/personal time for what is meant for- spending time. Cedar Row can help you</p>
    </div>
  </section>

  <section class="card back">
    <div class="services maintenance">
      <h2>Services We Include:</h2>
      <ul>
        <li>Lighting and plumbing repairs</li>
        <li>Ceiling fan installation</li>
        <li>Handicap accessories</li>
        <li>Locks and security</li>
        <li>Picture hanging</li>
        <li>Hang blinds</li>
        <li>Furniture arrangement / assembly</li>
        <li>Pressure washing</li>
        <li>Battery Jump start, and more...</li>
      </ul>
    </div>

    <div class="services concierge">
      <h2>Our Concierge<br>Services Include:</h2>
      <ul>
        <li>Errand running</li>
        <li>Grocery shopping</li>
        <li>Wellness Checks</li>
        <li>Dog Walk</li>
        <li>Garbage Collection,</li>
        <li class="more">and more...</li>
      </ul>
    </div>

    <div class="offer-banner">
      <svg width="533" height="27" viewBox="0 0 533 27" aria-hidden="true">
        <defs>
          <linearGradient id="bannerFill" x1="0" x2="1" y1="0" y2="0">
            <stop offset="0" stop-color="#2f2f31"/>
            <stop offset="0.55" stop-color="#3a2a2d"/>
            <stop offset="0.8" stop-color="#b42a36"/>
            <stop offset="1" stop-color="#e8303d"/>
          </linearGradient>
        </defs>
        <polygon points="0,0 533,0 533,27 0,27 12,13.5" fill="url(#bannerFill)"/>
      </svg>
      <span>We offer monthly service agreements and 24/7 access</span>
    </div>

    <div class="contact-prompt">Call text or e-mail<br>for more information</div>
    <div class="contact-divider"></div>

    <div class="contact-line phone">
      <svg width="30" height="22" viewBox="0 0 30 22" aria-hidden="true">
        <path d="M2 9 C2 2 28 2 28 9 L28 11 L21 11 L21 7 L9 7 L9 11 L2 11 Z" fill="#e1323e"/>
        <path d="M7 12 L23 12 L26 21 L4 21 Z" fill="#e1323e"/>
        <circle cx="15" cy="16" r="3" fill="#f6efd2"/>
      </svg>
      <span>704.555.0187</span>
    </div>
    <div class="contact-line email">
      <svg width="28" height="19" viewBox="0 0 28 19" aria-hidden="true">
        <rect x="0" y="0" width="28" height="19" rx="2" fill="#e1323e"/>
        <path d="M1 1 L14 11 L27 1 M1 18 L10 9 M27 18 L18 9" stroke="#f6efd2" stroke-width="1.6" fill="none"/>
      </svg>
      <span>1cedarrowmaint@quillpostmail.com</span>
    </div>
  </section>

  <div class="side-label back-label">back</div>
</div>
</body>
</html>
```